Brolvane Co.,Ltd. need business card

Brolvane Company Limited is a facility management company. We provides a total solution services from administration, energy saving, security, safety, food catering to companies.

The logo should be in elegant style with innovative that suited to the upper market
Please see the logo image in the attached file. You can use this Red or Blue or Green checkerboard (color and font should be similar to logo) as the main part of business card (can be an entire of one side of business card) . In another side of card should contain contact details of personnel - here below demo information

Kanyarat Thoengsai
Chief Executive Officer

No.73, Soi 5, Ruam Wongsa Road
Nong Khaem, Bangkok,
10520, Thailand

Tel + 66841537296
Mobile + 66841537296
E-mail: Kanyarat.Thoengsai@brolvane-example.co.th

Target Market(s)

Factory, Hotel and Hospital

Industry/Entity Type

Business

Contact Information for Business Card

Kanyarat Thoengsai
Chief Executive Officer

Nong Khaem, Bangkok,
10520, Thailand

Tel + 66841537296
Mobile + 66841537296

We will change details with the winner designer

Font styles to use
Sans Serif

Requirements
Must have
• In style of red checkerboard and white color

```html
<!DOCTYPE html>
<html lang="en">
<head>
<meta charset="utf-8">
<title>Brolvane Co.,Ltd. — Business Card</title>
<link rel="stylesheet" href="https://fonts.googleapis.com/css2?family=Old+Standard+TT:wght@400&family=PT+Sans:ital,wght@0,400;0,700;1,400&display=swap">
<style>
  :root {
    --brand-red: #990000;
    --accent-red: #d81e1e;
    --ink: #1a1a1a;
    --paper: #ffffff;
    --canvas: #ffffff;
  }
  * { margin: 0; padding: 0; box-sizing: border-box; }
  html, body {
    width: 1200px;
    height: 1000px;
    overflow: hidden;
    background: var(--canvas);
  }
  .stage { position: relative; width: 1200px; height: 1000px; }

  .card {
    position: absolute;
    width: 555px;
    height: 380px;
    background: var(--paper);
    overflow: hidden;
    outline: 1px solid #e4e4e4;
  }
  .card--front { left: 188px; top: 115px; }
  .card--back  { left: 465px; top: 516px; background: var(--brand-red); outline: none; }

  .pattern-fill {
    position: absolute;
    background: var(--brand-red);
  }
  .card--front .pattern-fill { left: 0; top: 0; width: 555px; height: 123px; }
  .card--back .pattern-fill { inset: 0; }

  .wordmark {
    position: absolute;
    left: 0;
    width: 100%;
    text-align: center;
    color: var(--paper);
    font-family: "Old Standard TT", serif;
    font-weight: 400;
    line-height: 1;
    text-transform: uppercase;
  }
  .card--front .wordmark { top: 50px; font-size: 40px; letter-spacing: 4px; }
  .card--back .wordmark  { top: 164px; font-size: 52px; letter-spacing: 7px; }

  .person {
    position: absolute;
    left: 75px;
    top: 227px;
    font-family: "PT Sans", sans-serif;
    color: var(--ink);
  }
  .person__name { font-size: 17px; font-weight: 700; line-height: 20px; }
  .person__title { font-size: 14px; font-style: italic; line-height: 18px; }

  .divider {
    position: absolute;
    left: 242px;
    top: 196px;
    width: 1.5px;
    height: 102px;
    background: var(--accent-red);
  }

  .contact {
    position: absolute;
    left: 262px;
    top: 199px;
    font-family: "PT Sans", sans-serif;
    font-size: 10.5px;
    line-height: 13.5px;
    color: var(--ink);
    list-style: none;
  }
  .contact__item { position: relative; padding-left: 18px; margin-bottom: 7px; }
  .contact__icon {
    position: absolute;
    left: 0;
    width: 11px;
    height: 11px;
  }
  .contact__item--address .contact__icon { top: 6px; }
  .contact__item--phone .contact__icon { top: 7px; }
  .contact__item--email .contact__icon { top: 2px; }
</style>
</head>
<body>
<main class="stage">

  <section class="card card--front" aria-label="Business card, contact side">
    <div class="pattern-fill" role="img" aria-label="Red checkerboard pattern band"></div>
    <div class="wordmark">Brolvane</div>

    <div class="person">
      <p class="person__name">Kanyarat Thoengsai</p>
      <p class="person__title">Chief Executive Officer</p>
    </div>

    <div class="divider"></div>

    <ul class="contact">
      <li class="contact__item contact__item--address">
        <svg class="contact__icon" viewBox="0 0 12 12" aria-hidden="true">
          <path d="M6 0.8a4 4 0 0 0-4 4c0 3 4 6.6 4 6.6s4-3.6 4-6.6a4 4 0 0 0-4-4z" fill="none" stroke="var(--accent-red)" stroke-width="1.4"/>
          <circle cx="6" cy="4.8" r="1.4" fill="var(--accent-red)"/>
        </svg>
        No.73, Soi 5, Ruam Wongsa Road<br>
        Nong Khaem, Bangkok,<br>
        10520, Thailand
      </li>
      <li class="contact__item contact__item--phone">
        <svg class="contact__icon" viewBox="0 0 12 12" aria-hidden="true">
          <path d="M2.3 1c.5-.4 1.1-.3 1.4.2l1 1.7c.3.5.1 1-.3 1.3l-.6.4c.5 1.3 1.4 2.3 2.6 2.9l.5-.6c.3-.4.9-.5 1.3-.2l1.6 1.1c.5.3.5 1 .1 1.4l-.8.8C7.6 11.3 1 5.4 1.5 2z" fill="var(--accent-red)"/>
        </svg>
        Tel + 66841537296<br>
        Mobile + 66841537296
      </li>
      <li class="contact__item contact__item--email">
        <svg class="contact__icon" viewBox="0 0 12 9" aria-hidden="true">
          <rect x="0" y="0.5" width="12" height="8" fill="var(--accent-red)"/>
          <path d="M0.5 1l5.5 4 5.5-4" fill="none" stroke="#fff" stroke-width="1"/>
        </svg>
        E-mail: Kanyarat.Thoengsai@brolvane-example.co.th
      </li>
    </ul>
  </section>

  <section class="card card--back" aria-label="Business card, brand side">
    <div class="pattern-fill" role="img" aria-label="Red checkerboard pattern covering the card"></div>
    <div class="wordmark">Brolvane</div>
  </section>

</main>
</body>
</html>
```